Business Card Design

We just need these details on one side of card and logo on the other.

Industry/Entity Type

Business

Contact Information for Business Card

Colette Marsh | Artist
87 Tillbrook Lane
Dunmore Heights Vic 3172
# 0418 207 913 | 03 9386 2417
colette@colettemarsh-example.com
colettesstudio-example.com.au

```html
<!DOCTYPE html>
<html lang="en">
<head>
<meta charset="utf-8">
<title>Colette's Studio – Business Cards</title>
<link rel="stylesheet" href="https://fonts.googleapis.com/css2?family=Montserrat:wght@300;400;600&display=swap">
<style>
  :root {
    --backdrop: #d9d9d9;
    --card: #141414;
    --ink: #f2f2f2;
    --ink-soft: #bdbdbd;
    --rule: #8a8a8a;
  }
  * { margin: 0; padding: 0; box-sizing: border-box; }
  html, body {
    width: 1200px; height: 988px; overflow: hidden;
    background: var(--backdrop);
    font-family: "Montserrat", sans-serif;
    color: var(--ink);
  }
  .sheet {
    position: relative; width: 1200px; height: 988px;
    display: flex; flex-direction: column; align-items: center; justify-content: center; gap: 40px;
  }
  .card {
    position: relative; width: 760px; height: 434px;
    background: var(--card);
    box-shadow: 0 6px 18px rgba(0,0,0,.25);
    overflow: hidden;
  }
  .brand-name {
    position: absolute;
    font-weight: 300; letter-spacing: 1px; color: var(--ink);
    line-height: 1; white-space: nowrap;
  }

  .card-front .brand-name {
    left: 0; right: 0; top: 180px; text-align: center; font-size: 68px;
  }

  .card-back .brand-name { left: 60px; top: 96px; font-size: 42px; }
  .top-rule {
    position: absolute; left: 500px; right: 40px; top: 118px; height: 1px; background: var(--rule);
  }

  .person { position: absolute; left: 60px; top: 226px; }
  .person-name { font-size: 22px; font-weight: 600; letter-spacing: 1px; white-space: nowrap; }
  .person-title { font-size: 11px; font-weight: 300; letter-spacing: 2px; color: var(--ink-soft); margin-top: 4px; }

  .contact-list { position: absolute; list-style: none; }
  .contact-list li {
    display: flex; align-items: center; gap: 12px;
    height: 34px; font-size: 12px; font-weight: 300; letter-spacing: .3px;
    white-space: nowrap;
    border-bottom: 1px solid var(--rule);
    padding-bottom: 4px; margin-bottom: 6px;
  }
  .contact-list .icon { width: 20px; height: 20px; background: var(--ink); flex: none; }
  .contact-left { left: 60px; top: 290px; width: 350px; }
  .contact-right { left: 440px; top: 160px; width: 280px; }
</style>
</head>
<body>
<main class="sheet">
  <section class="card card-front" aria-label="Card front">
    <p class="brand-name">Colette's Studio</p>
  </section>

  <section class="card card-back" aria-label="Card back">
    <p class="brand-name">Colette's Studio</p>
    <div class="top-rule"></div>
    <div class="person">
      <p class="person-name">COLETTE MARSH</p>
      <p class="person-title">ARTIST</p>
    </div>
    <ul class="contact-list contact-left">
      <li><span class="icon"></span>0418 207 913</li>
      <li><span class="icon"></span>03 9386 2417</li>
      <li><span class="icon"></span>87 Tillbrook Lane, Dunmore Heights Vic 3172</li>
    </ul>
    <ul class="contact-list contact-right">
      <li><span class="icon"></span>colette@colettemarsh-example.com</li>
      <li><span class="icon"></span>colettesstudio-example.com.au</li>
    </ul>
  </section>
</main>
</body>
</html>
```